Website Re-design and extension of an existing website

I have a Wordpress website currently and I need it to be upgraded. I have MOST of the content to get it started and the rest (video's, pictures ect) are on the way. I want to know if it is possible to convert my existing website into a Personal Brand website with a public speaking emphasis. I would like to have my website modeled after the following website:

http://www.vandolake.example/

I have attached a document entitled "Website Outline & Content" that has all of the text on it and it has red headlines that indicate where something needs to be added or designed. I will be happy to give more detail if needed.

Things I still need to get to you in order to design the website;

-Demo video
-Full length public speaking video

Target Market(s)

Corporations, universities, trade associations, private events

Coding

Coded - Design and coding required

Requirements
Must have
• Pictures, links, downloadable forms, MULTIPLE video's embedded, my logo, keep the colors in sync with my existing marketing material
Nice to have
• I would like my design colors thematic as already inherent in my marketing materials (see my Speaker One Sheet)

```html
<!DOCTYPE html>
<html lang="en">
<head>
<meta charset="utf-8">
<title>Brant Calloway — Your Holistic Lifestyle Hacker</title>
<link href="https://fonts.googleapis.com/css2?family=Hind:wght@400;500;600;700&family=Abril+Fatface&family=Yellowtail&display=swap" rel="stylesheet">
<style>
:root{
  --olive:#6b7237;
  --olive-dark:#5a5f38;
  --olive-btn:#a29d5c;
  --ink:#444;
  --muted:#8a8a8a;
  --bar:#2d2d2d;
  --red:#e0483a;
  --teal:#4fa39d;
  --amber:#f3a62a;
  --paper:#f3f3f1;
  --white:#fff;
}
*{margin:0;padding:0;box-sizing:border-box}
html,body{width:858px;height:1200px;overflow:hidden}
body{position:relative;font-family:"Hind",sans-serif;color:var(--ink);background:var(--white)}
.abs{position:absolute}

/* header */
.site-header{left:0;top:0;width:858px;height:49px;background:var(--white);border-bottom:1px solid #ddd}
.brand{left:80px;top:12px;display:flex;align-items:center;gap:6px}
.brand-dot{width:24px;height:24px;border-radius:50%;background:var(--olive)}
.brand-name{font-weight:700;font-size:15px;color:var(--olive);line-height:1}
.brand-tag{font-weight:700;font-size:6px;color:var(--olive);letter-spacing:.3px;margin-top:2px}
.main-nav{left:222px;top:18px;display:flex;gap:13px;font-size:7.3px;color:#888;border-top:1px solid #eee;padding-top:6px}
.main-nav .active{color:var(--olive)}
.social-tiles{left:726px;top:0;width:50px;height:49px;display:grid;grid-template-columns:1fr 1fr;gap:1px;background:var(--white)}
.social-tiles span{background:var(--olive-dark);display:flex;align-items:center;justify-content:center}
.social-tiles span i{width:6px;height:6px;border-radius:50%;background:var(--white);display:block}

/* hero */
.hero{left:0;top:49px;width:858px;height:335px;background:linear-gradient(180deg,#8a6f5e 0%,#a0705a 28%,#4e4a40 55%,#2f3230 100%)}
.hero-script{left:186px;top:58px;font-family:"Yellowtail",cursive;font-size:27px;color:var(--white)}
.hero-title{left:116px;top:90px;font-family:"Abril Fatface",serif;font-size:33px;color:var(--white);display:flex;gap:8px;align-items:center}
.hero-title .boxed{background:var(--white);color:#2c2c2c;padding:0 6px;line-height:1.05}
.hero-sub{left:169px;top:138px;font-size:10px;color:var(--white)}
.hero-cta{left:176px;top:163px;width:136px;height:22px;background:#6e7a45;color:var(--white);font-size:7.5px;display:flex;align-items:center;justify-content:center;gap:6px;border-radius:2px}
.hero-cta i{width:9px;height:9px;border-radius:50%;background:var(--white);display:block}
.sheet{top:201px;width:120px;text-align:center;color:var(--white);font-size:7.8px}
.sheet .disc{width:50px;height:50px;border-radius:50%;margin:0 auto 14px;display:flex;align-items:center;justify-content:center}

/* tabs */
.tab-bar{left:0;top:384px;width:858px;height:26px;background:var(--bar);display:flex;justify-content:center;align-items:center;font-size:7.5px;color:var(--white)}
.tab-bar span{padding:0 13px;border-left:1px solid #555;line-height:14px}
.tab-bar span:first-child{border:0}
.tab-bar .active{background:var(--white);color:#555;line-height:26px;position:relative;top:-3px;height:29px;padding-top:1px}

/* about */
.about-photo{left:0;top:410px;width:195px;height:248px;background:linear-gradient(90deg,#9a9a9a 0%,#c4c4c4 70%,#f5f5f5 100%)}
.about-title{left:196px;top:465px;font-size:13.5px;font-weight:500;color:var(--olive);letter-spacing:.3px}
.about-copy{left:196px;top:494px;width:326px;font-size:6.9px;line-height:11.8px;color:#555}
.read-more{left:196px;top:593px;width:57px;height:19px;background:var(--olive);color:var(--white);font-size:6px;font-weight:600;letter-spacing:1px;display:flex;align-items:center;justify-content:center}
.laptop{left:508px;top:427px;width:350px;height:231px}
.video-frame{left:563px;top:446px;width:295px;height:185px;background:linear-gradient(135deg,#5b4636 0%,#c9b59a 45%,#8a5a44 100%)}
.play{left:687px;top:520px;width:38px;height:38px;background:#e02020;border-radius:6px;display:flex;align-items:center;justify-content:center}

/* testimonials */
.testimonials{left:0;top:658px;width:858px;height:279px;background:var(--paper)}
.t-kicker{left:0;top:684px;width:858px;text-align:center;font-size:7.5px;color:#555}
.t-title{left:0;top:696px;width:858px;text-align:center;font-size:15px;font-weight:600;color:var(--olive)}
.t-card{left:219px;top:738px;width:420px;height:158px;background:var(--white);border:1px solid #e4e4e4}
.t-quote-mark{left:252px;top:722px;font-family:"Abril Fatface",serif;font-size:52px;color:#e2e2e2}
.t-avatar{left:402px;top:720px;width:54px;height:54px;border-radius:50%;background:linear-gradient(#cfd6dc,#5b6570);border:3px solid var(--white);box-shadow:0 0 0 1px #ddd}
.t-text{left:236px;top:785px;width:386px;text-align:center;font-size:6.7px;line-height:12.3px;color:#888}
.t-cite{left:219px;top:869px;width:420px;text-align:center;font-size:7px;color:#555}
.t-arrow{top:810px}
.dots{left:416px;top:909px;display:flex;gap:5px}
.dots i{width:4px;height:4px;border-radius:50%;background:#8b9553;display:block}
.dots i:first-child{background:#333}

/* partners */
.partners{left:0;top:937px;width:858px;height:36px;background:var(--white);display:flex;justify-content:space-around;align-items:center;padding:0 60px}
.partners i{display:block;background:#c8c8c8;height:10px;width:50px;border-radius:2px}

/* footer */
.site-footer{left:0;top:973px;width:858px;height:227px;background:var(--olive-dark)}
.f-brand{left:0;top:992px;width:858px;text-align:center;color:var(--white)}
.f-brand .disc{width:44px;height:44px;border-radius:50%;background:var(--white);margin:0 auto 6px}
.f-brand .name{font-weight:700;font-size:18px;line-height:1}
.f-brand .tag{font-size:6px;font-weight:700;letter-spacing:.4px;margin-top:3px}
.signup{left:252px;top:1083px;width:354px;height:23px;display:flex}
.signup .field{flex:1;background:var(--white);font-size:6.8px;color:#777;display:flex;align-items:center;padding-left:10px}
.signup .btn{width:52px;background:var(--olive-btn);color:var(--white);font-size:6.5px;font-weight:700;display:flex;align-items:center;justify-content:center}
.f-social{left:0;top:1136px;width:858px;display:flex;justify-content:center;gap:11px}
.f-social i{width:5px;height:5px;border-radius:50%;background:#d6d6c4;display:block}
.f-nav{left:0;top:1157px;width:858px;text-align:center;font-size:7px;color:var(--white)}
.f-nav b{font-weight:400;margin:0 5px}
.f-legal{left:0;top:1172px;width:858px;text-align:center;font-size:6.5px;color:var(--white)}
.to-top{left:776px;top:1152px;width:28px;height:28px;border-radius:50%;background:var(--white);display:flex;align-items:center;justify-content:center}
</style>
</head>
<body>

<header class="site-header abs">
  <div class="brand abs">
    <span class="brand-dot"></span>
    <div><div class="brand-name">Brant Calloway</div><div class="brand-tag">YOUR HOLISTIC LIFESTYLE HACKER</div></div>
  </div>
  <nav class="main-nav abs">
    <span class="active">Home</span><span>About us</span><span>Motivational Speaker/Keynote</span><span>Workshop Presenter</span><span>Author</span><span>Coaching</span><span>Blog</span><span>Online Courses</span><span>Contact Brant Calloway</span>
  </nav>
  <div class="social-tiles abs"><span><i></i></span><span><i></i></span><span><i></i></span><span><i></i></span></div>
</header>

<section class="hero abs" role="img" aria-label="Photo of the speaker smiling, leaning on a wooden bridge railing with mountains at sunset behind"></section>
<div class="hero-script abs">Your Holistic</div>
<h1 class="hero-title abs"><span>Lifestyle</span><span class="boxed">Hacker</span></h1>
<p class="hero-sub abs">Lose Your Mind &amp; Find Your Health!</p>
<div class="hero-cta abs">See How Brant Calloway Can Help <i></i></div>

<div class="sheet abs" style="left:64px"><div class="disc" style="background:var(--red)"><svg width="22" height="22" viewBox="0 0 22 22" fill="none" stroke="#fff" stroke-width="2.4"><path d="M11 2v11M6 8l5 5 5-5M3 15v4h16v-4"/></svg></div>Brant's Speaker One Sheet</div>
<div class="sheet abs" style="left:173px"><div class="disc" style="background:var(--teal)"><svg width="22" height="22" viewBox="0 0 22 22" fill="none" stroke="#fff" stroke-width="2.4"><path d="M11 2v11M6 8l5 5 5-5M3 15v4h16v-4"/></svg></div>Brant's Media Sheet</div>
<div class="sheet abs" style="left:280px;width:140px"><div class="disc" style="background:var(--amber)"><svg width="22" height="22" viewBox="0 0 22 22" fill="none" stroke="#fff" stroke-width="2.4"><path d="M11 2v11M6 8l5 5 5-5M3 15v4h16v-4"/></svg></div>Brant's College Speaker One Sheet</div>

<nav class="tab-bar abs">
  <span class="active">Brant Calloway</span><span>Sugar Addiction Expert</span><span>Holistic Health Expert</span><span>Author &amp; Speaker</span>
</nav>

<div class="about-photo abs" role="img" aria-label="Black and white portrait of the speaker"></div>
<h2 class="about-title abs">ABOUT BRANT CALLOWAY</h2>
<p class="about-copy abs">For over 17 years, Brant Calloway has tirelessly helped executives, employees, and everyday people achieve lasting health and fitness by helping them “lose their minds.” Using his unique 4-Quadrant Coaching System, speaking platform, and online training courses, Brant has helped hundreds of people shed their limiting beliefs, eat better, shed sugar addiction and transform their bodies and minds. Brant delights in helping people see through the self-deception of being “normal,” and he invites his students to discover and accept the extraordinary people they truly are. If you are ready to transform physically, mentally, emotionally, and spiritually, it is time for you to meet Brant Calloway, your Holistic Health Hacker!</p>
<div class="read-more abs">READ MORE ::</div>

<svg class="laptop abs" viewBox="0 0 350 231" aria-hidden="true">
  <path d="M50 14 Q50 4 62 4 H350 V210 H50 Z" fill="#e9e9e9" stroke="#9a9a9a"/>
  <circle cx="202" cy="11" r="2" fill="#333"/>
  <path d="M0 222 L50 210 H350 V231 H20 Z" fill="#cfcfcf" stroke="#999"/>
</svg>
<div class="video-frame abs" role="img" aria-label="Video still of children holding pet rabbits"></div>
<div class="play abs"><svg width="14" height="16" viewBox="0 0 14 16"><path d="M1 1 L13 8 L1 15 Z" fill="#fff"/></svg></div>

<section class="testimonials abs"></section>
<div class="t-kicker abs">what others say about</div>
<h2 class="t-title abs">Testimonials</h2>
<div class="t-card abs"></div>
<div class="t-quote-mark abs">“</div>
<div class="t-avatar abs" role="img" aria-label="Portrait of the reviewer"></div>
<p class="t-text abs">An important aspect of a successful and highly effective workforce is good health. Brant Calloway of Evergreen Wellness provides a wealth of knowledge trough his FitPath and Sugar Addiction Courses that has visibly changed the lives of many of the executives at Summit Ridge. He brought a whole new level of understanding on good nutrition and the pitfalls of certain poor food choices. But that is just the beginning of the training. Brant has trained the staff on good sleep habits, stress management, and exercise. All of this has been combined with individual one-on-one training with staff and their spouses. The individual coaching is flexible and targeted on areas that will most benefit the participants.</p>
<p class="t-cite abs">-Warren Dabney, CEO Summit Ridge Credit Union</p>
<svg class="t-arrow abs" style="left:173px" width="10" height="16" viewBox="0 0 10 16"><path d="M8 2 L2 8 L8 14" fill="none" stroke="#444" stroke-width="1.6"/></svg>
<svg class="t-arrow abs" style="left:675px" width="10" height="16" viewBox="0 0 10 16"><path d="M2 2 L8 8 L2 14" fill="none" stroke="#444" stroke-width="1.6"/></svg>
<div class="dots abs"><i></i><i></i><i></i></div>

<div class="partners abs"><i></i><i style="width:16px"></i><i style="width:56px"></i><i style="width:20px"></i><i style="width:14px;height:14px;border-radius:50%"></i><i style="width:24px"></i><i style="width:46px"></i><i style="width:40px"></i></div>

<footer class="site-footer abs"></footer>
<div class="f-brand abs">
  <div class="disc"></div>
  <div class="name">Brant Calloway</div>
  <div class="tag">YOUR HOLISTIC LIFESTYLE HACKER</div>
</div>
<form class="signup abs"><div class="field">Get Brant Calloway Branding Secrets Now</div><div class="btn">SUBSCRIBE</div></form>
<div class="f-social abs"><i></i><i></i><i></i><i></i><i></i><i></i></div>
<div class="f-nav abs">Home<b>|</b>About us<b>|</b>Motivational Speaker/Keynote<b>|</b>Workshop Presenter<b>|</b>Author<b>|</b>Coaching<b>|</b>Blog<b>|</b>Online Courses<b>|</b>Contact Brant Calloway</div>
<div class="f-legal abs">© Copyright 2017 &nbsp;Privacy Policy &nbsp;:: &nbsp;Terms of Use &nbsp;:: &nbsp;Cookies Policy</div>
<div class="to-top abs"><svg width="16" height="18" viewBox="0 0 16 18"><path d="M8 17 V3 M2 9 L8 2 L14 9" fill="none" stroke="#5a5f38" stroke-width="3"/></svg></div>

</body>
</html>
```